Larkspur Ridge Management - Business Cards

I need business cards. My current logo was designed by a designer at this site and I very much like and am happy with the results. I would like a business card that is trendy, unique, current yet professional. I deal with high net worth clients daily

Target Market(s)

Out of state investors looking to get into the rental market in Ohio

Industry/Entity Type

Property Management, Consulting

Contact Information for Business Card

Name, Title (Chief Financial Officer) office phone number (555) 817-3094 website address larkridgemgmt.example

Font styles to use
Sans Serif

Colors
0054AA
0677BA
7BADD7
CADEEF
E8F1F8
0094D4
00A9DD
6FCCEA
C7EBF8
E9F6FB
00AB8E
00BBA5
67D7C9
C6EFE9
E9F9F6

```html
<!DOCTYPE html>
<html lang="en">
<head>
<meta charset="utf-8">
<title>Larkspur Ridge Management – Business Card</title>
<link rel="stylesheet" href="https://fonts.googleapis.com/css2?family=Nunito:wght@800;900&family=Roboto+Condensed:wght@400;500&display=swap">
<style>
  :root {
    --card-front-bg: #E8F1F8;
    --brand-blue: #1857A6;
    --name-blue: #1A4FA3;
    --title-grey: #555555;
    --label-teal: #00BBA5;
    --value-blue: #1A4FA3;
    --white: #FFFFFF;
  }
  * { margin: 0; padding: 0; box-sizing: border-box; }
  html, body {
    width: 1200px;
    height: 343px;
    overflow: hidden;
    background: var(--white);
  }
  .canvas {
    position: relative;
    width: 1200px;
    height: 343px;
    display: flex;
  }
  .card-front {
    position: relative;
    width: 600px;
    height: 343px;
    background: var(--card-front-bg);
  }
  .card-back {
    position: relative;
    width: 600px;
    height: 343px;
    background: var(--brand-blue);
    display: flex;
    align-items: center;
    justify-content: center;
  }
  .wordmark {
    display: flex;
    flex-direction: column;
    align-items: center;
    gap: 10px;
    font-family: "Nunito", sans-serif;
    font-weight: 900;
    text-align: center;
    line-height: 1.05;
    letter-spacing: 0.5px;
  }
  .wordmark-square {
    width: 34px;
    height: 34px;
  }
  .wordmark-text { font-size: 27px; }
  .card-front .wordmark {
    position: absolute;
    left: 20px;
    top: 90px;
    width: 214px;
    color: var(--brand-blue);
  }
  .card-front .wordmark-square { background: var(--brand-blue); }
  .card-back .wordmark { color: var(--white); width: 260px; }
  .card-back .wordmark-square { background: var(--white); }
  .card-back .wordmark-text { font-size: 32px; }
  .divider {
    position: absolute;
    left: 257px;
    top: 18px;
    width: 1.5px;
    height: 307px;
    background: var(--name-blue);
  }
  .contact-block {
    position: absolute;
    left: 282px;
    top: 110px;
  }
  .person-name {
    font-family: "Nunito", sans-serif;
    font-weight: 900;
    font-size: 17.5px;
    letter-spacing: 0.6px;
    color: var(--name-blue);
    text-transform: uppercase;
  }
  .person-title {
    margin-top: 4px;
    font-family: "Roboto Condensed", sans-serif;
    font-weight: 500;
    font-size: 14.5px;
    color: var(--title-grey);
  }
  .contact-list {
    margin-top: 18px;
    display: grid;
    grid-template-columns: 80px auto;
    row-gap: 7px;
    font-family: "Roboto Condensed", sans-serif;
    font-size: 15px;
  }
  .contact-label { color: var(--label-teal); font-weight: 500; }
  .contact-value { color: var(--value-blue); font-weight: 400; }
</style>
</head>
<body>
  <main class="canvas">
    <section class="card-front">
      <div class="wordmark">
        <span class="wordmark-square"></span>
        <span class="wordmark-text">Larkspur Ridge Management</span>
      </div>
      <div class="divider"></div>
      <div class="contact-block">
        <h1 class="person-name">Marcus Whitfield</h1>
        <p class="person-title">Chief Financial Officer</p>
        <dl class="contact-list">
          <dt class="contact-label">Office phone:</dt>
          <dd class="contact-value">(555) 817-3094</dd>
          <dt class="contact-label">Website:</dt>
          <dd class="contact-value">larkridgemgmt.example</dd>
        </dl>
      </div>
    </section>
    <section class="card-back">
      <div class="wordmark">
        <span class="wordmark-square"></span>
        <span class="wordmark-text">Larkspur Ridge Management</span>
      </div>
    </section>
  </main>
</body>
</html>
```